Dr. Marissa Tevlin Medical/Chiropractic Business Card

Dr. Tevlin is a chiropractor and will require a business card that she uses every single day to book appointments on the back side of the card. Currently the office name goes by Dr. Marissa Tevlin. The chiropractic profession is based on the diagnosis and manipulative treatment of misalignments of the joints, especially those of the spinal column, which are held to cause other disorders by affecting the nerves, muscles, and organs. Dr. Marissa Tevlin is looking for a contemporary and minimalistic design.

Industry/Entity Type

Medical

Contact Information for Business Card

Name: Dr. Marissa Tevlin; Address: 748 Harcastle Rd South, London, ON N5R 2K7; Phone Number: 519.274.6193; Fax: 519.281.5046; email: marissa.tevlin@quorvamail.com

Requirements
Must have
• ability to write multiple appointments date/time on the back of card

```html
<!DOCTYPE html>
<html lang="en">
<head>
<meta charset="utf-8">
<title>Dr. Marissa Tevlin — Business Card</title>
<link rel="stylesheet" href="https://fonts.googleapis.com/css2?family=Arimo:wght@400;700&family=Josefin+Sans:wght@600;700&family=Roboto+Condensed:wght@700&display=swap">
<style>
  :root {
    --backdrop: #d1d2d4;
    --navy: #252a43;
    --white: #ffffff;
    --rule: #c9cbd4;
  }
  * { box-sizing: border-box; margin: 0; padding: 0; }
  html, body { width: 1200px; height: 1000px; overflow: hidden; }
  body { background: var(--backdrop); position: relative; font-family: "Arimo", Arial, sans-serif; color: var(--white); }
  .card { position: absolute; left: 229px; width: 744px; background: var(--navy); }
  .card-front { top: 48px; height: 425px; text-align: center; }
  .card-back { top: 528px; height: 425px; }

  .doctor-name { position: absolute; top: 88px; width: 100%; font-size: 36px; font-weight: 700; }
  .doctor-title { position: absolute; top: 131px; width: 100%; font-size: 29px; }
  .phone { position: absolute; top: 238px; width: 100%; font-size: 41px; font-weight: 700; letter-spacing: 2px; }
  .contact-line { position: absolute; top: 349px; width: 100%; font-size: 24px; }
  .divider { position: absolute; top: 402px; left: 40px; right: 40px; height: 1px; background: var(--rule); }
  .address { position: absolute; top: 414px; width: 100%; font-size: 27px; font-weight: 700; }

  .back-heading { position: absolute; top: 24px; width: 100%; text-align: center; font-family: "Josefin Sans", sans-serif; font-weight: 600; font-size: 38px; letter-spacing: 6px; }
  .schedule { position: absolute; left: 33px; top: 79px; width: 678px; height: 289px; background: var(--white); }
  .schedule svg { display: block; }
  .col-label { font-family: "Josefin Sans", sans-serif; font-weight: 700; font-size: 22px; letter-spacing: 2px; fill: var(--navy); }
  .footnote { position: absolute; top: 380px; width: 100%; text-align: center; font-family: "Roboto Condensed", sans-serif; font-weight: 700; font-size: 21px; }
</style>
</head>
<body>
  <section class="card card-front">
    <h1 class="doctor-name" style="top:40px">Dr. Marissa Tevlin</h1>
    <p class="doctor-title" style="top:84px">Chiropractor</p>
    <p class="phone" style="top:190px">519.274.6193</p>
    <p class="contact-line" style="top:301px">Fax: 519.281.5046, email: marissa.tevlin@quorvamail.com</p>
    <div class="divider" style="top:355px"></div>
    <p class="address" style="top:367px">748 Harcastle Rd South, London, ON N5R 2K7</p>
  </section>

  <section class="card card-back">
    <h2 class="back-heading">APPOINTMENTS</h2>
    <div class="schedule">
      <svg width="678" height="289" viewBox="0 0 678 289" aria-label="Appointment date and time lines">
        <text class="col-label" x="113" y="38" text-anchor="middle">DATE</text>
        <text class="col-label" x="268" y="38" text-anchor="middle">TIME</text>
        <text class="col-label" x="443" y="38" text-anchor="middle">DATE</text>
        <text class="col-label" x="598" y="38" text-anchor="middle">TIME</text>
        <line x1="339" y1="13" x2="339" y2="255" stroke="#252a43" stroke-width="3"/>
        <g stroke="#252a43" stroke-width="3">
          <path d="M29 74H200M223 74H318M360 74H531M553 74H648"/>
          <path d="M29 116H200M223 116H318M360 116H531M553 116H648"/>
          <path d="M29 160H200M223 160H318M360 160H531M553 160H648"/>
          <path d="M29 202H200M223 202H318M360 202H531M553 202H648"/>
          <path d="M29 246H200M223 246H318M360 246H531M553 246H648"/>
        </g>
      </svg>
    </div>
    <p class="footnote">If you are unable to make your appointment, please call us to reschedule</p>
  </section>
</body>
</html>
```